Modern card design needed for building development company

We are looking for a sharp modern new look for our business cards.
We are a New Zealand based company called TKV Ventures NZ LTD that specialises in subdividing large sections, housing and commercial buildings.
We have attached a photo of the current logo and would like to see it improved somehow as it looks a bit dated.
We are open to any colours.

Target Market(s)

Investors, Property buyers

Industry/Entity Type

Investment

Contact Information for Business Card

TKV VENTURES NZ LTD
www.tkvventuresnz.co.nz

Howard Pennick
Phone +64 21 843 192
Email hdpennick@fernmail.co.nz

Font styles to use
Serif
Sans Serif

Colors
0792cd
33a6d7
85cae6
6b449b
886aae
f04a50
ec1f27
f37122
f68d4d

Requirements
Must have
• Please try and make the logo more modern or if you have a similar one we would like to see it.

```html
<!DOCTYPE html>
<html lang="en">
<head>
<meta charset="utf-8">
<title>TKV Ventures NZ LTD – Business Card</title>
<link href="https://fonts.googleapis.com/css2?family=Open+Sans:wght@400;700&display=swap" rel="stylesheet">
<style>
  :root {
    --page-bg: #d9d9d9;
    --card-dark: #2a2829;
    --card-mid: #3a3839;
    --card-light: #5a5a5c;
    --accent: #f2c21b;
    --text-grey: #b9b9b9;
    --rule-grey: #6e6e6e;
  }
  html, body {
    margin: 0;
    width: 1200px;
    height: 873px;
    overflow: hidden;
    background: var(--page-bg);
    font-family: "Open Sans", Arial, sans-serif;
  }
  .canvas {
    position: relative;
    width: 1200px;
    height: 873px;
  }
  .card {
    position: absolute;
    top: 281px;
    width: 540px;
    height: 310px;
    border-radius: 4px;
    overflow: hidden;
    box-shadow: 0 6px 18px rgba(0,0,0,.25);
  }
  /* Front: contact side */
  .card--front {
    left: 40px;
    background: linear-gradient(160deg, var(--card-light) 0%, var(--card-mid) 40%, var(--card-dark) 100%);
  }
  .card__shards {
    position: absolute;
    left: 0;
    top: 0;
    width: 250px;
    height: 150px;
    background: radial-gradient(ellipse at 20% 35%, rgba(150,150,152,.55) 0%, rgba(110,110,112,.3) 45%, rgba(60,60,62,0) 75%);
  }
  .card__swoosh {
    position: absolute;
    left: 0;
    top: 0;
    width: 540px;
    height: 310px;
  }
  .contact {
    position: absolute;
    left: 270px;
    top: 36px;
    width: 250px;
  }
  .brand {
    display: flex;
    align-items: center;
    gap: 10px;
  }
  .brand__square {
    width: 24px;
    height: 24px;
    border: 2px solid var(--accent);
    box-sizing: border-box;
    flex: none;
  }
  .brand__name {
    color: var(--accent);
    font-weight: 700;
    font-size: 17px;
    letter-spacing: .3px;
    white-space: nowrap;
  }
  .person {
    margin: 14px 0 18px 34px;
    color: var(--accent);
    font-weight: 700;
    font-size: 12px;
    letter-spacing: .5px;
    text-transform: uppercase;
  }
  .contact__list {
    list-style: none;
    margin: 0;
    padding: 0 0 0 34px;
  }
  .contact__item {
    display: flex;
    align-items: center;
    gap: 10px;
    height: 28px;
    color: var(--text-grey);
    font-size: 12px;
  }
  .contact__icon {
    width: 14px;
    height: 14px;
    flex: none;
  }
  /* Back: brand side */
  .card--back {
    left: 620px;
    background: radial-gradient(ellipse at 50% 40%, var(--card-mid) 0%, var(--card-dark) 80%);
  }
  .back__rule {
    position: absolute;
    left: 0;
    top: 0;
  }
  .back__mark {
    position: absolute;
    left: 240px;
    top: 100px;
    width: 60px;
    height: 60px;
    border: 3px solid var(--accent);
    box-sizing: border-box;
    background: var(--card-dark);
  }
  .back__name {
    position: absolute;
    left: 0;
    top: 182px;
    width: 540px;
    text-align: center;
    color: var(--accent);
    font-weight: 700;
    font-size: 20px;
    letter-spacing: .4px;
  }
</style>
</head>
<body>
<main class="canvas">

  <section class="card card--front" aria-label="Business card, contact side">
    <div class="card__shards" role="img" aria-label="Shattered grey fragments decoration"></div>
    <svg class="card__swoosh" viewBox="0 0 540 310" aria-hidden="true">
      <path d="M0 150 Q 120 300 420 310 L0 310 Z" fill="#4a4a4c"/>
      <path d="M0 150 Q 120 300 420 310" fill="none" stroke="#6a6a6c" stroke-width="2"/>
    </svg>
    <div class="contact">
      <div class="brand">
        <span class="brand__square"></span>
        <span class="brand__name">TKV VENTURES NZ LTD</span>
      </div>
      <div class="person">Howard Pennick</div>
      <ul class="contact__list">
        <li class="contact__item">
          <svg class="contact__icon" viewBox="0 0 14 14" aria-hidden="true"><path d="M3 1 L5.5 1 L6.5 4 L5 5.2 Q6.3 8 8.8 9 L10 7.5 L13 8.5 L13 11 Q12 13 9.5 12.5 Q3 10.5 1.5 4 Q1 2 3 1 Z" fill="#f2c21b"/></svg>
          <span>+64 21 843 192</span>
        </li>
        <li class="contact__item">
          <svg class="contact__icon" viewBox="0 0 14 14" aria-hidden="true"><rect x="1" y="3" width="12" height="8" fill="#f2c21b"/><path d="M1 3 L7 8 L13 3" fill="none" stroke="#2a2829" stroke-width="1.2"/></svg>
          <span>hdpennick@fernmail.co.nz</span>
        </li>
        <li class="contact__item">
          <svg class="contact__icon" viewBox="0 0 14 14" aria-hidden="true"><circle cx="7" cy="7" r="6" fill="#f2c21b"/><ellipse cx="7" cy="7" rx="2.5" ry="6" fill="none" stroke="#2a2829" stroke-width="1"/><path d="M1 7 H13" stroke="#2a2829" stroke-width="1"/></svg>
          <span>www.tkvventuresnz.co.nz</span>
        </li>
      </ul>
    </div>
  </section>

  <section class="card card--back" aria-label="Business card, brand side">
    <svg class="back__rule" width="540" height="310" viewBox="0 0 540 310" aria-hidden="true">
      <line x1="0" y1="130" x2="540" y2="130" stroke="#6e6e6e" stroke-width="2"/>
      <rect x="100" y="121" width="26" height="18" fill="#6e6e6e"/>
      <rect x="414" y="121" width="26" height="18" fill="#6e6e6e"/>
    </svg>
    <div class="back__mark"></div>
    <div class="back__name">TKV VENTURES NZ LTD</div>
  </section>

</main>
</body>
</html>
```